Hearth Table Cover Design

Open to creative ideas, we don't have a set cover style in mind so have fun with it!
Front Cover for Ebook-Quorvex and vantor shelf. Book title is "Hearth Table" sub title is "A Gentle Map for Kitchen Rhythms", Author is Corinne L Waddell. Website is www.theolwynkitchenworks.com.
Open to creative ideas, we dont' have a set cover style in mind so have fun with it!
We have attached some pictures of Corinne which could be incorporated into the title. We can send you high def files if you need.
We have attached two book covers which we like to get you started, but feel free to have fun, we're looking for something creative and catchy

```html
<!DOCTYPE html>
<html lang="en">
<head>
<meta charset="utf-8">
<title>Hearth Table – Front Cover</title>
<link rel="stylesheet" href="https://fonts.googleapis.com/css2?family=Dancing+Script:wght@400&family=Open+Sans:wght@300&family=Cinzel:wght@400&display=swap">
<style>
  :root {
    --stage: #ebeced;
    --paper: #ffffff;
    --author-teal: #5f9c8e;
    --title-ink: #1b1b1b;
    --title-red: #9a1c25;
    --subtitle-slate: #5b67a0;
    --portrait-light: #e9d6c4;
    --portrait-mid: #6f9a86;
    --portrait-deep: #46648a;
    --food-gold: #e9b45a;
    --food-berry: #c2445a;
    --food-green: #7ea54a;
    --food-cream: #f3efe6;
  }
  * { box-sizing: border-box; margin: 0; padding: 0; }
  html, body {
    width: 1200px;
    height: 900px;
    overflow: hidden;
    background: var(--stage);
  }
  .canvas {
    position: relative;
    width: 1200px;
    height: 900px;
  }
  .cover {
    position: absolute;
    left: 338px;
    top: 20px;
    width: 524px;
    height: 860px;
    background: var(--paper);
    overflow: hidden;
    box-shadow: 0 2px 14px rgba(0, 0, 0, 0.12);
  }
  .author {
    position: absolute;
    top: 30px;
    left: 0;
    width: 100%;
    text-align: center;
    font-family: "Dancing Script", cursive;
    font-size: 32px;
    color: var(--author-teal);
    letter-spacing: 1px;
  }
  .title {
    position: absolute;
    top: 100px;
    left: 0;
    width: 100%;
    text-align: center;
    line-height: 1;
    font-weight: 400;
  }
  .title-top {
    display: block;
    font-family: "Open Sans", sans-serif;
    font-weight: 300;
    font-size: 54px;
    color: var(--title-ink);
    letter-spacing: 1px;
  }
  .title-bottom {
    display: block;
    margin-top: 4px;
    font-family: "Cinzel", serif;
    font-weight: 400;
    font-size: 54px;
    color: var(--title-red);
    letter-spacing: 1px;
  }
  .subtitle {
    position: absolute;
    top: 262px;
    left: 222px;
    width: 182px;
    font-family: "Open Sans", sans-serif;
    font-weight: 300;
    font-size: 29px;
    line-height: 1.15;
    color: var(--subtitle-slate);
    text-align: center;
  }
  .author-portrait {
    position: absolute;
    left: 0;
    top: 250px;
    width: 215px;
    height: 610px;
    border-radius: 100px 100px 0 0;
    background: linear-gradient(180deg,
      var(--portrait-light) 0%,
      var(--portrait-light) 24%,
      var(--portrait-mid) 38%,
      var(--portrait-mid) 60%,
      var(--portrait-deep) 70%,
      var(--portrait-deep) 100%);
  }
  .food-stack {
    position: absolute;
    left: 412px;
    top: 300px;
    width: 112px;
    height: 480px;
    border-radius: 56px 0 40px 40px;
    background: linear-gradient(180deg,
      var(--food-green) 0%,
      var(--food-berry) 18%,
      var(--food-gold) 38%,
      var(--food-gold) 62%,
      var(--food-cream) 100%);
  }
</style>
</head>
<body>
  <main class="canvas">
    <section class="cover">
      <div class="author-portrait" role="img" aria-label="Photograph of the author, Corinne L Waddell, standing in a green t-shirt and jeans"></div>
      <div class="food-stack" role="img" aria-label="Photograph of stacked bowls of cereal and berries wrapped in a measuring tape, with a honey jar and a jug of milk"></div>
      <p class="author">Corinne L Waddell</p>
      <h1 class="title">
        <span class="title-top">HEARTH</span>
        <span class="title-bottom">TABLE</span>
      </h1>
      <p class="subtitle">A Gentle Map for Kitchen Rhythms</p>
    </section>
  </main>
</body>
</html>
```